Modern & Fresh Sumeray Book Cover

Need a creative e-book cover for my book.

Title: Get Sumeray Sorted
Subtitle: Learn How To Easily Choose & Enroll in the Perfect Coverage at the Perfect Time.

Target Market(s)

60-70 year olds in the United States

Font styles to use
Sans Serif

Colors
9bcb3c
33a6d7

Requirements
Must have
• Must look modern and fresh.
• Use our company colors www.BrovaMint.com

```html
<!DOCTYPE html>
<html lang="en">
<head>
<meta charset="utf-8">
<title>Get Sumeray Sorted – Book Cover</title>
<link rel="stylesheet" href="https://fonts.googleapis.com/css2?family=Oswald:wght@700&family=Montserrat:wght@400;600;700&family=Mr+Dafoe&display=swap">
<style>
  :root {
    --backdrop: #14abbb;
    --paper: #ffffff;
    --brand-green: #9bcb3c;
    --brand-blue: #33a6d7;
    --ink: #1a1a1a;
    --photo-light: #f4f1ee;
    --photo-mid: #d9cbbd;
    --photo-dark: #8c7462;
  }
  * { margin: 0; padding: 0; box-sizing: border-box; }
  html, body {
    width: 1200px; height: 1200px; overflow: hidden;
    background: var(--backdrop);
  }
  .stage {
    position: relative; width: 1200px; height: 1200px;
  }
  .cover {
    position: absolute; left: 360px; top: 240px;
    width: 480px; height: 720px;
    background: var(--paper);
    overflow: hidden;
  }
  .cover-photo {
    position: absolute; left: 60px; top: 228px;
    width: 360px; height: 318px;
    background: radial-gradient(ellipse at 50% 55%, var(--photo-mid) 0%, var(--photo-light) 60%, var(--paper) 78%);
  }
  .cover-photo::after {
    content: ""; position: absolute; left: 30px; right: 30px; bottom: 10px; height: 80px;
    background: radial-gradient(ellipse at 50% 60%, rgba(60,50,45,0.35) 0%, rgba(255,255,255,0) 70%);
  }
  .title-main {
    position: absolute; left: 0; right: 0; top: 32px;
    text-align: center;
    font-family: "Oswald", sans-serif; font-weight: 700;
    font-size: 56px; line-height: 1; letter-spacing: -1px;
    color: var(--brand-green); text-transform: uppercase;
  }
  .title-script {
    position: absolute; left: 0; right: 0; top: 78px;
    text-align: center;
    font-family: "Mr Dafoe", cursive;
    font-size: 150px; line-height: 1;
    color: var(--brand-blue);
    transform: rotate(-4deg);
  }
  .subtitle {
    position: absolute; left: 0; right: 0; top: 558px;
    text-align: center;
    font-family: "Montserrat", sans-serif; font-weight: 400;
    font-size: 17px; line-height: 24px; color: var(--ink);
  }
  .subtitle .accent-green { color: var(--brand-green); font-weight: 700; }
  .subtitle .accent-blue { color: var(--brand-blue); font-weight: 700; }
  .publisher {
    position: absolute; left: 0; right: 0; top: 640px;
    text-align: center;
    font-family: "Montserrat", sans-serif; font-weight: 700;
    font-size: 32px; line-height: 1; color: var(--brand-green);
    letter-spacing: -0.5px;
  }
</style>
</head>
<body>
  <main class="stage">
    <section class="cover">
      <div class="cover-photo" role="img" aria-label="Photo of a smiling older couple riding a white tandem bicycle, the woman waving"></div>
      <h1 class="title-main">Get Sumeray</h1>
      <div class="title-script">Sorted</div>
      <p class="subtitle">Learn How To <span class="accent-green">Easily Choose &amp; Enroll</span><br><span class="accent-blue">in the Perfect Coverage</span> at the Perfect Time</p>
      <div class="publisher">BrovaMint</div>
    </section>
  </main>
</body>
</html>
```